pet resort day care for our buisiness

we need a new web design for our pet center in Florida , we are provide the following services -
1. dog day car
2.dog/cat boarding
3. dog grooming
4. Dog training
5.pet food toy and clothing
our current websit is -http://www.tallowfieldanimalhaven.example/
we are looking for a fresh new design that will reflect the change that we have made in the vusness from renovationnto the facelaty new management and new servises
Target Market(s)
Dog Lover , Upmarket
Industry/Entity Type
Pet
Number of Pages Required
5+ page
Font styles to use
Sans Serif
Requirements
Must have
- clean design , easy to understand and navigate , our target is the upmarket costumer how are dog lover
Should not have
- NOOO of the shelf design , confusing design , brown colors

```html
<!DOCTYPE html>
<html lang="en">
<head>
<meta charset="utf-8">
<title>Tallowfield Animal Haven</title>
<link rel="stylesheet" href="https://fonts.googleapis.com/css2?family=Open+Sans:wght@400;600;700;800&family=Dancing+Script:wght@700&display=swap">
<style>
:root{
  --pink:#ec3b6a;
  --pink-dark:#d42d5b;
  --ink:#1c1c1c;
  --nav:#111111;
  --text:#555555;
  --muted:#8a8a8a;
  --light:#f4f4f4;
  --footer:#2a2a2a;
  --footer-bottom:#1d1d1d;
  --white:#ffffff;
  --water-top:#7fb3c9;
  --water-bottom:#3f7f99;
}
*{box-sizing:border-box;margin:0;padding:0}
html,body{width:795px;height:1200px;overflow:hidden}
body{font-family:"Open Sans",Arial,sans-serif;background:var(--white);color:var(--text);position:relative}
a{color:inherit;text-decoration:none}

.top-bar{height:45px;position:relative;background:var(--white)}
.social{position:absolute;left:14px;top:11px;display:flex;gap:6px}
.social span{width:22px;height:22px;border-radius:50%;background:var(--pink);display:block}
.top-contact{position:absolute;right:18px;top:8px;text-align:left}
.top-contact .name{font-size:11px;color:var(--ink);font-weight:600}
.top-contact .phone{font-size:15px;color:var(--pink);font-weight:800}

.brand{position:absolute;left:50%;top:0;transform:translateX(-50%);width:150px;height:150px;border-radius:50%;background:var(--white);z-index:5;display:flex;flex-direction:column;align-items:center;justify-content:center;box-shadow:0 2px 6px rgba(0,0,0,.15)}
.brand .mark{width:40px;height:40px;border-radius:50%;background:var(--pink);margin-bottom:8px}
.brand .brand-name{font-size:15px;font-weight:800;color:var(--pink);text-align:center;line-height:1.15;width:120px}

.main-nav{height:24px;background:var(--nav);display:flex;justify-content:space-between;padding:0 30px;align-items:center}
.main-nav ul{list-style:none;display:flex;gap:22px}
.main-nav li{color:var(--white);font-size:11px;font-weight:600}
.main-nav li.active{color:var(--pink)}

.hero{position:relative;height:368px;background:linear-gradient(180deg,#9cc6a0 0%,var(--water-top) 22%,var(--water-bottom) 100%)}
.hero-arrow{position:absolute;top:160px;width:26px;height:26px;border-radius:50%;background:rgba(255,255,255,.85);display:flex;align-items:center;justify-content:center}
.hero-arrow.prev{left:16px}.hero-arrow.next{right:16px}
.hero-caption{position:absolute;left:210px;bottom:44px;font-family:"Dancing Script",cursive;color:var(--white);font-size:38px;line-height:1.05;text-shadow:0 2px 4px rgba(0,0,0,.35)}
.hero-caption span{display:block;padding-left:60px}

.features{height:68px;background:var(--light);display:flex;justify-content:space-around;align-items:center;padding:0 30px}
.feature{display:flex;align-items:center;gap:10px}
.feature svg{flex:none}
.feature h3{font-size:15px;color:var(--pink);font-weight:700}
.feature p{font-family:"Dancing Script",cursive;font-size:14px;color:var(--muted)}

.welcome{text-align:center;padding:28px 90px 0}
.welcome h2{font-family:"Dancing Script",cursive;font-size:28px;color:var(--ink)}
.welcome h2 em{font-style:normal;color:var(--pink)}
.welcome .lead{font-size:12px;color:var(--ink);margin-top:10px;line-height:1.55}
.welcome .body{font-size:10px;color:var(--muted);margin-top:10px;line-height:1.6}
.btn-more{display:inline-block;margin-top:16px;border:1px solid #bbb;font-size:9px;font-weight:700;padding:6px 18px;color:var(--muted);letter-spacing:.5px}

.services{display:flex;justify-content:center;gap:46px;margin-top:42px}
.service{text-align:center;width:96px}
.service-art{width:74px;height:74px;border-radius:50%;border:2px dashed var(--pink);margin:0 auto;background:radial-gradient(circle,#fbe1e8 0%,#ffffff 70%)}
.service h4{font-size:24px;font-weight:800;color:var(--ink);margin-top:10px;line-height:1}
.service p{font-family:"Dancing Script",cursive;color:var(--pink);font-size:16px}

.cta{position:absolute;left:0;top:933px;width:100%;height:74px;background:var(--pink);display:flex;align-items:center;padding:0 30px;color:var(--white)}
.cta-book{display:flex;align-items:center;gap:10px;width:50%}
.cta-book .label{font-family:"Dancing Script",cursive;font-size:19px}
.cta-book .phone{font-size:30px;font-weight:800;letter-spacing:.5px;line-height:1}
.cta-news{display:flex;align-items:center;gap:10px}
.cta-news .label{font-family:"Dancing Script",cursive;font-size:19px;display:block;margin-bottom:6px}
.news-form{display:flex}
.news-form .field{width:170px;height:26px;background:var(--white);color:#aaa;font-size:10px;padding:6px 8px}
.news-form .submit{height:26px;background:var(--ink);color:var(--white);font-size:10px;font-weight:700;padding:7px 12px}

.site-footer{position:absolute;left:0;top:1007px;width:100%;height:158px;background:var(--footer);display:flex;padding:18px 30px 0;gap:34px;color:#c9c9c9}
.footer-brand{width:150px;display:flex;flex-direction:column;align-items:center;padding-top:10px}
.footer-brand .mark{width:34px;height:34px;border-radius:50%;background:var(--pink);margin-bottom:8px}
.footer-brand .brand-name{font-size:15px;font-weight:800;color:var(--white);text-align:center;line-height:1.2}
.footer-col h5{font-size:12px;color:var(--white);font-weight:700;margin-bottom:10px;padding-bottom:6px;border-bottom:2px solid var(--pink);display:inline-block}
.footer-col ul{list-style:none;font-size:10px;line-height:1.85}
.links{display:flex;gap:34px}
.hours p{font-size:10px;line-height:1.55}
.contact li{display:flex;gap:7px;align-items:flex-start;margin-bottom:4px}
.contact svg{flex:none;margin-top:3px}

.footer-bottom{position:absolute;left:0;top:1165px;width:100%;height:35px;background:var(--footer-bottom);font-size:9px;color:#888;display:flex;align-items:center;justify-content:center}
</style>
</head>
<body>

<header class="top-bar">
  <div class="social" aria-label="Social links"><span></span><span></span><span></span><span></span></div>
  <div class="top-contact">
    <div class="name">Tallowfield Animal Haven</div>
    <div class="phone">954-555-0186</div>
  </div>
</header>

<div class="brand">
  <span class="mark"></span>
  <span class="brand-name">Tallowfield Animal Haven</span>
</div>

<nav class="main-nav">
  <ul><li class="active">Home</li><li>Boarding</li><li>Daycare</li><li>Grooming</li></ul>
  <ul><li>Training</li><li>Boutique</li><li>Blog</li><li>About Us</li></ul>
</nav>

<section class="hero" role="img" aria-label="Photo of a happy dog splashing through shallow lake water">
  <span class="hero-arrow prev"><svg width="10" height="10" viewBox="0 0 10 10"><path d="M7 1 3 5l4 4" stroke="#333" stroke-width="2" fill="none"/></svg></span>
  <span class="hero-arrow next"><svg width="10" height="10" viewBox="0 0 10 10"><path d="M3 1l4 4-4 4" stroke="#333" stroke-width="2" fill="none"/></svg></span>
  <p class="hero-caption">Love to play and<span>meet my buddies.</span></p>
</section>

<section class="features">
  <div class="feature">
    <svg width="30" height="30" viewBox="0 0 30 30"><rect x="4" y="6" width="22" height="20" rx="2" fill="none" stroke="#ec3b6a" stroke-width="2"/><path d="M4 12h22M10 3v6M20 3v6" stroke="#ec3b6a" stroke-width="2"/></svg>
    <div><h3>Reservations</h3><p>What time is best for you?</p></div>
  </div>
  <div class="feature">
    <svg width="30" height="30" viewBox="0 0 30 30"><circle cx="15" cy="15" r="12" fill="none" stroke="#ec3b6a" stroke-width="2"/><path d="M15 8v14M11 11h6a3 3 0 0 1 0 6h-4" stroke="#ec3b6a" stroke-width="2" fill="none"/></svg>
    <div><h3>Our Rates</h3><p>Boarding, Daycare, Grooming</p></div>
  </div>
  <div class="feature">
    <svg width="30" height="30" viewBox="0 0 30 30"><path d="M6 11h18l-2 15H8z" fill="none" stroke="#ec3b6a" stroke-width="2"/><path d="M11 11a4 4 0 0 1 8 0" stroke="#ec3b6a" stroke-width="2" fill="none"/></svg>
    <div><h3>Boutique &amp; Holistic</h3><p>High Quality Pet Products</p></div>
  </div>
</section>

<section class="welcome">
  <h2>Welcome to <em>Tallowfield Animal Haven!</em></h2>
  <p class="lead">A pet paradise providing the best pet care in the greater Fort Lauderdale FL area. Professional cat &amp; dog boarding, doggy daycare, pet grooming, training, holistic foods &amp; pet boutique.</p>
  <p class="body">Discover how much our haven has to offer for your beloved pet. Our calm, air-conditioned suites and a bright outdoor playground with a splash pool keep every guest happy, active and well cared for while you are away from home.</p>
  <a class="btn-more" href="#">LEARN MORE</a>
</section>

<section class="services">
  <div class="service"><div class="service-art" role="img" aria-label="Illustrated dog for day care"></div><h4>DOG</h4><p>day care</p></div>
  <div class="service"><div class="service-art" role="img" aria-label="Illustrated dog and cat for boarding"></div><h4>DOG/CAT</h4><p>boarding</p></div>
  <div class="service"><div class="service-art" role="img" aria-label="Illustrated dog for grooming"></div><h4>DOG</h4><p>grooming</p></div>
  <div class="service"><div class="service-art" role="img" aria-label="Illustrated dog for training"></div><h4>DOG</h4><p>training</p></div>
  <div class="service"><div class="service-art" role="img" aria-label="Illustrated dog for pet food and toys"></div><h4>PET FOOD</h4><p>toy &amp; clothing</p></div>
</section>

<section class="cta">
  <div class="cta-book">
    <svg width="30" height="30" viewBox="0 0 30 30"><rect x="4" y="6" width="22" height="20" rx="2" fill="none" stroke="#fff" stroke-width="2"/><path d="M4 12h22M10 3v6M20 3v6" stroke="#fff" stroke-width="2"/></svg>
    <div><span class="label">Book an Appointment Today! Call us now</span><div class="phone">954-555-0186</div></div>
  </div>
  <div class="cta-news">
    <svg width="30" height="30" viewBox="0 0 30 30"><rect x="3" y="7" width="24" height="16" rx="2" fill="none" stroke="#fff" stroke-width="2"/><path d="M3 8l12 9 12-9" stroke="#fff" stroke-width="2" fill="none"/></svg>
    <div><span class="label">Subscribe Our Newsletter!!</span>
      <div class="news-form"><span class="field">Enter Email Address</span><span class="submit">SIGN UP NOW</span></div>
    </div>
  </div>
</section>

<footer class="site-footer">
  <div class="footer-brand"><span class="mark"></span><span class="brand-name">Tallowfield Animal Haven</span></div>
  <div class="footer-col">
    <h5>Quick Links</h5>
    <div class="links">
      <ul><li>Home</li><li>Boarding</li><li>Daycare</li><li>Grooming</li><li>Training</li></ul>
      <ul><li>Boutique</li><li>Blog</li><li>About Us</li><li>Contact</li></ul>
    </div>
  </div>
  <div class="footer-col hours">
    <h5>Hours of Operations</h5>
    <p>Open 7 days</p><p>per week</p><br>
    <p>Monday - Saturday</p><p>7:00 am to 7:00 pm</p><br>
    <p>Sunday</p><p>9:00 am to 5:00 pm</p>
  </div>
  <div class="footer-col contact">
    <h5>Get in Touch</h5>
    <ul>
      <li><svg width="10" height="12" viewBox="0 0 10 12"><path d="M5 0a4 4 0 0 1 4 4c0 3-4 8-4 8S1 7 1 4a4 4 0 0 1 4-4z" fill="#ec3b6a"/></svg><span>210 Harbor Palm Way,<br>Fort Lauderdale, FL 33316</span></li>
      <li><svg width="10" height="12" viewBox="0 0 10 12"><path d="M2 0h2l1 3-1.5 1a6 6 0 0 0 3 3L8 6l2 1v2c0 1-1 2-2 2C4 11 0 7 0 2 0 1 1 0 2 0z" fill="#ec3b6a"/></svg><span>Call Us<br>954-555-0186</span></li>
      <li><svg width="10" height="12" viewBox="0 0 10 12"><rect x="0" y="2" width="10" height="8" fill="#ec3b6a"/></svg><span>Email Us<br>info@tallowfieldanimalhaven.example</span></li>
    </ul>
  </div>
</footer>

<div class="footer-bottom">Copyright © 2024 Tallowfield Animal Haven. All rights reserved. | Privacy Policy | Sitemap</div>

</body>
</html>
```